Brightvolt Electrical Services Needs A Flyer Design

We need a flyer design for a new business based in Sydney, Australia called Brightvolt Electrical Services. We provide services for residential,commercial and industrial works. Services include Electrical Design, Installation, Repairs & Maintenance. Communications Installation, Cabling, Maintenance & Repairs. Over 25 years Industry Experience.Service Calls, Quick Response Time, Professional Service. We would like to see designs that use the colors red,white and blue similar to the logo. The final Design should be creative as the business logo suggests and should communicate the businesses services.

Target Market(s)

Residential

Industry/Entity Type

Industrial

Font styles to use
Sans Serif

Requirements
Must have
• My project must have the logo provided utilized in the flyer.It must list the following contact name and number Ray 0491 627 318 services as above in the project description. Flyer should be DL size (99mmx210mm).

```html
<!DOCTYPE html>
<html lang="en">
<head>
<meta charset="utf-8">
<title>Brightvolt Electrical Services – DL Flyers</title>
<link rel="stylesheet" href="https://fonts.googleapis.com/css2?family=Open+Sans:wght@400;600;700&display=swap">
<style>
  :root {
    --backdrop: #ece9e4;
    --brand-blue: #2b3a8f;
    --brand-red: #e31e2d;
    --brand-navy: #1c2b5a;
    --white: #ffffff;
    --band-text-light: #fde4e6;
    --band-text-pink: #f7b8bf;
  }
  * { box-sizing: border-box; margin: 0; padding: 0; }
  html, body {
    width: 956px; height: 1200px; overflow: hidden;
    background: var(--backdrop);
    font-family: "Open Sans", Arial, sans-serif;
  }
  .canvas { position: relative; width: 956px; height: 1200px; }
  .flyer { position: absolute; width: 373px; box-shadow: 0 2px 6px rgba(0,0,0,.18); }
  .flyer svg { display: block; }
  .flyer--services { left: 95px; top: 68px; height: 790px; }
  .flyer--benefits { left: 535px; top: 340px; height: 793px; }

  .brand-name { font-weight: 700; fill: var(--brand-navy); }
  .band-text { font-weight: 600; font-size: 15.5px; text-anchor: middle; }
  .band-text--light { fill: var(--band-text-light); }
  .band-text--pink { fill: var(--band-text-pink); }
  .services-heading { font-weight: 400; font-size: 21px; fill: var(--brand-red); }
  .list-item { font-weight: 400; fill: var(--white); }
  .tagline { font-weight: 400; font-size: 12.5px; fill: var(--white); text-anchor: middle; }
  .contact-name { font-weight: 700; font-size: 29px; fill: var(--white); text-anchor: middle; }
  .contact-phone { font-weight: 700; font-size: 23px; fill: var(--white); text-anchor: middle; }
</style>
</head>
<body>
<main class="canvas">

  <!-- Flyer one: services list -->
  <article class="flyer flyer--services">
    <svg width="373" height="790" viewBox="0 0 373 790">
      <defs>
        <linearGradient id="planGrad" x1="0" y1="0" x2="1" y2="1">
          <stop offset="0" stop-color="#f1f2f3"/>
          <stop offset="1" stop-color="#b9bec5"/>
        </linearGradient>
        <linearGradient id="terminalGrad" x1="0" y1="0" x2="0" y2="1">
          <stop offset="0" stop-color="#6d6a62"/>
          <stop offset="1" stop-color="#d9d5cc"/>
        </linearGradient>
      </defs>

      <rect class="photo photo--plans" x="0" y="0" width="373" height="480" fill="url(#planGrad)"
            role="img" aria-label="Photo: architectural floor plans with calculator, scale ruler, pencils and compass"/>

      <g class="logo" transform="translate(186,248)">
        <text class="brand-name" x="0" y="0" font-size="29" letter-spacing="2" text-anchor="middle">BRIGHTVOLT</text>
        <text class="brand-name" x="0" y="16" font-size="10" letter-spacing="1.5" text-anchor="middle">ELECTRICAL SERVICES</text>
      </g>

      <polygon points="0,404 373,268 373,272 0,408" fill="var(--white)"/>
      <polygon class="band band--red" points="0,408 373,272 373,334 0,470" fill="var(--brand-red)"/>
      <polygon points="0,470 373,334 373,790 0,790" fill="var(--white)"/>

      <polygon class="photo photo--terminals" points="0,476 134,428 134,790 0,790" fill="url(#terminalGrad)"
               role="img" aria-label="Photo: wired terminal blocks in an electrical panel"/>
      <polygon class="panel panel--blue" points="139,456 373,371 373,790 139,790" fill="var(--brand-blue)"/>
      <polygon points="139,664 373,579 373,584 139,669" fill="var(--white)"/>

      <g class="band-copy" transform="translate(186,375) rotate(-20)">
        <text class="band-text band-text--light" x="0" y="-4">ELECTRICAL SERVICES FOR RESIDENTIAL,</text>
        <text class="band-text band-text--light" x="0" y="14">COMMERCIAL AND INDUSTRIAL WORKS</text>
      </g>

      <g class="services" transform="translate(153,502) rotate(-20)">
        <circle cx="16" cy="-40" r="10" fill="var(--brand-red)"/>
        <path d="M12,-45 L19,-40 L12,-35" fill="none" stroke="var(--white)" stroke-width="2"/>
        <text class="services-heading" x="33" y="-33">Services:</text>
        <text class="list-item" font-size="15" x="0" y="0">» Electrical Design</text>
        <text class="list-item" font-size="15" x="-9" y="26">» Electrical Installation</text>
        <text class="list-item" font-size="15" x="-19" y="52">» Communications Installation</text>
        <text class="list-item" font-size="15" x="-28" y="78">» Cabling</text>
        <text class="list-item" font-size="15" x="-38" y="104">» Repairs &amp; Maintenance</text>
      </g>

      <g class="contact">
        <text class="tagline" transform="translate(262,662) rotate(-20)">Your Neighborhood Electrician</text>
        <text class="contact-name" transform="translate(273,712) rotate(-20)">Ray</text>
        <g transform="translate(282,746) rotate(-20)">
          <g transform="translate(-94,-20)">
            <path d="M2,10 Q13,1 24,10 L21,14 L17,12 L17,9 Q13,7 9,9 L9,12 L5,14 Z M6,15 L20,15 L23,22 L3,22 Z" fill="var(--white)"/>
            <circle cx="13" cy="18" r="2.4" fill="var(--brand-blue)"/>
          </g>
          <text class="contact-phone" x="14" y="0">0491 627 318</text>
        </g>
      </g>
    </svg>
  </article>

  <!-- Flyer two: benefits list -->
  <article class="flyer flyer--benefits">
    <svg width="373" height="793" viewBox="0 0 373 793">
      <defs>
        <linearGradient id="cableGrad" x1="0" y1="0" x2="1" y2="1">
          <stop offset="0" stop-color="#ffffff"/>
          <stop offset="0.6" stop-color="#eef0f2"/>
          <stop offset="1" stop-color="#c9d6e4"/>
        </linearGradient>
        <linearGradient id="rackGrad" x1="0" y1="0" x2="0" y2="1">
          <stop offset="0" stop-color="#3b4048"/>
          <stop offset="1" stop-color="#a3a9b1"/>
        </linearGradient>
      </defs>

      <rect class="photo photo--cable" x="0" y="0" width="373" height="480" fill="url(#cableGrad)"
            role="img" aria-label="Photo: blue network cable with connector plug"/>

      <rect x="30" y="58" width="262" height="70" fill="var(--white)"/>
      <g class="logo" transform="translate(161,96)">
        <text class="brand-name" x="0" y="0" font-size="29" letter-spacing="2" text-anchor="middle">BRIGHTVOLT</text>
        <text class="brand-name" x="0" y="16" font-size="10" letter-spacing="1.5" text-anchor="middle">ELECTRICAL SERVICES</text>
      </g>

      <polygon points="0,410 373,274 373,278 0,414" fill="var(--white)"/>
      <polygon class="band band--blue" points="0,414 373,278 373,338 0,474" fill="var(--brand-blue)"/>
      <polygon points="0,474 373,338 373,793 0,793" fill="var(--white)"/>

      <polygon class="photo photo--rack" points="0,480 158,422 158,793 0,793" fill="url(#rackGrad)"
               role="img" aria-label="Photo: patch panels and network cabling in a server rack"/>
      <polygon class="panel panel--red" points="163,420 373,344 373,793 163,793" fill="var(--brand-red)"/>
      <polygon points="163,672 373,596 373,601 163,677" fill="var(--white)"/>

      <g class="band-copy" transform="translate(186,380) rotate(-20)">
        <text class="band-text band-text--pink" x="0" y="-4">ELECTRICAL SERVICES FOR RESIDENTIAL,</text>
        <text class="band-text band-text--pink" x="0" y="14">COMMERCIAL AND INDUSTRIAL WORKS</text>
      </g>

      <g class="benefits" transform="translate(172,466) rotate(-20)">
        <text class="list-item" font-size="16" x="0" y="0">» Over 25 years Industry</text>
        <text class="list-item" font-size="16" x="8" y="19">Experience</text>
        <text class="list-item" font-size="16" x="-15" y="42">» Service Calls</text>
        <text class="list-item" font-size="16" x="-31" y="84">» Quick Response Time</text>
        <text class="list-item" font-size="16" x="-46" y="126">» Professional Service</text>
      </g>

      <g class="contact">
        <text class="tagline" transform="translate(278,664) rotate(-20)">Your Neighborhood Electrician</text>
        <text class="contact-name" transform="translate(268,712) rotate(-20)">Ray</text>
        <g transform="translate(284,744) rotate(-20)">
          <g transform="translate(-94,-20)">
            <path d="M2,10 Q13,1 24,10 L21,14 L17,12 L17,9 Q13,7 9,9 L9,12 L5,14 Z M6,15 L20,15 L23,22 L3,22 Z" fill="var(--white)"/>
            <circle cx="13" cy="18" r="2.4" fill="var(--brand-red)"/>
          </g>
          <text class="contact-phone" x="14" y="0">0491 627 318</text>
        </g>
      </g>
    </svg>
  </article>

</main>
</body>
</html>
```